Larkspur Ridge Management - Business Cards

I need business cards. My current logo was designed by a designer at this site and I very much like and am happy with the results. I would like a business card that is trendy, unique, current yet professional. I deal with high net worth clients daily

Target Market(s)

Out of state investors looking to get into the rental market in Ohio

Industry/Entity Type

Property Management, Consulting

Contact Information for Business Card

Name, Title (Chief Financial Officer) office phone number (555) 817-3094 website address larkridgemgmt.example

Font styles to use
Sans Serif

Colors
0054AA
0677BA
7BADD7
CADEEF
E8F1F8
0094D4
00A9DD
6FCCEA
C7EBF8
E9F6FB
00AB8E
00BBA5
67D7C9
C6EFE9
E9F9F6

```html
<!DOCTYPE html>
<html lang="en">
<head>
<meta charset="utf-8">
<title>Larkspur Ridge Management – Business Cards</title>
<link href="https://fonts.googleapis.com/css2?family=Arimo:wght@400;700&display=swap" rel="stylesheet">
<style>
  :root{
    --stage:#3f3f3f;
    --card-white:#ffffff;
    --brand-blue:#0054aa;
    --mid-blue:#0677ba;
    --sky:#00a9dd;
    --teal:#00bba5;
    --light-teal:#67d7c9;
    --text-grey:#6a6a6a;
    --rule-grey:#c9c9c9;
  }
  *{margin:0;padding:0;box-sizing:border-box;}
  html,body{width:1200px;height:1200px;overflow:hidden;}
  body{background:var(--stage);position:relative;font-family:"Arimo",Arial,sans-serif;}

  .card{position:absolute;width:689px;height:393px;border-radius:26px;overflow:hidden;}
  .card--front{left:266px;top:158px;background:var(--card-white);}
  .card--back{left:262px;top:653px;background:var(--brand-blue);}

  .brand{position:absolute;display:flex;flex-direction:column;align-items:center;}
  .brand__mark{display:block;}
  .brand__name{font-weight:700;text-transform:uppercase;text-align:center;line-height:1.1;}

  .card--front .brand{left:66px;top:89px;width:280px;}
  .card--front .brand__mark{width:64px;height:64px;background:var(--teal);margin-bottom:18px;}
  .card--front .brand__name{font-size:29px;color:var(--brand-blue);}

  .card--back .brand{left:0;top:44px;width:100%;}
  .card--back .brand__mark{width:104px;height:104px;background:var(--light-teal);margin-bottom:26px;}
  .card--back .brand__name{font-size:46px;color:var(--card-white);}

  .divider{position:absolute;left:348px;top:81px;width:1px;height:233px;background:var(--rule-grey);}

  .person{position:absolute;left:387px;top:108px;}
  .person__name{font-size:27px;font-weight:700;color:var(--brand-blue);letter-spacing:0.5px;line-height:1.1;}
  .person__title{font-size:15.5px;color:var(--text-grey);margin-top:4px;}

  .contact{position:absolute;left:387px;top:201px;list-style:none;}
  .contact__item{display:flex;align-items:center;height:20.5px;font-size:16.5px;color:var(--text-grey);}
  .contact__icon{width:14px;height:14px;margin-right:12px;flex:none;fill:var(--sky);}
</style>
</head>
<body>

<section class="card card--front">
  <div class="brand">
    <span class="brand__mark"></span>
    <div class="brand__name">Larkspur<br>Ridge<br>Management</div>
  </div>
  <div class="divider"></div>
  <div class="person">
    <h1 class="person__name">JORDAN HALE</h1>
    <p class="person__title">Chief Financial Officer</p>
  </div>
  <ul class="contact">
    <li class="contact__item">
      <svg class="contact__icon" viewBox="0 0 24 24"><path d="M6.6 10.8a15.1 15.1 0 0 0 6.6 6.6l2.2-2.2c.3-.3.7-.4 1-.2 1.1.4 2.3.6 3.6.6.6 0 1 .4 1 1V20c0 .6-.4 1-1 1A17 17 0 0 1 3 4c0-.6.4-1 1-1h3.5c.6 0 1 .4 1 1 0 1.3.2 2.5.6 3.6.1.3 0 .7-.2 1z"/></svg>
      (555) 817-3094
    </li>
    <li class="contact__item">
      <svg class="contact__icon" viewBox="0 0 24 24"><path d="M2 5h20v14H2z M4 7v1l8 5 8-5V7l-8 5z" fill-rule="evenodd"/></svg>
      info@larkridgemgmt.example
    </li>
    <li class="contact__item">
      <svg class="contact__icon" viewBox="0 0 24 24"><circle cx="12" cy="12" r="10"/><path d="M8 5c2 1 1 3 3 4s0 3-2 3-3 2-2 4M15 14c2-1 4 0 4 2" stroke="#fff" stroke-width="1.6" fill="none"/></svg>
      www.larkridgemgmt.example
    </li>
  </ul>
</section>

<section class="card card--back">
  <div class="brand">
    <span class="brand__mark"></span>
    <div class="brand__name">Larkspur<br>Ridge<br>Management</div>
  </div>
</section>

</body>
</html>
```